Personal Real Estate Brochure

I would like a brochure design that matches my team branding but also has a light and airy feeling to it. The industry I'm in is real estate, so some real estate type images and icons would be great. I will attach some of the branding that needs to be in the brochure. Looking to have this be the start of a marketing relationship for other projects. Need this brochure to be in a format that I will be able to edit, so a Microsoft office compatible program would be great.

Here is our website.
www.teamhollowbrook.ca

Sections that need to be in there are:
Mission Statement
Bio
Why Use a Buyer's Agent
Choosing the right realtor

If you think other ones let me know and we can work together in completing them.

```html
<!DOCTYPE html>
<html lang="en">
<head>
<meta charset="utf-8">
<title>Clara Whitfield – Real Estate Brochure</title>
<link href="https://fonts.googleapis.com/css2?family=Montserrat:ital,wght@0,400;0,600;0,700;0,800;1,400&family=Open+Sans:wght@400;600;700&display=swap" rel="stylesheet">
<style>
  :root {
    --red: #d4252e;
    --green: #1f9a4a;
    --leaf: #8cc63f;
    --ink: #3a3a3a;
    --muted: #666;
    --paper: #ffffff;
    --paper-alt: #f3f3f3;
    --backdrop: #e9e9e9;
  }
  * { box-sizing: border-box; margin: 0; padding: 0; }
  html, body { width: 1200px; height: 795px; overflow: hidden; }
  body {
    background: var(--backdrop);
    font-family: "Open Sans", Arial, sans-serif;
    color: var(--ink);
    position: relative;
  }
  .brochure {
    position: absolute;
    left: 60px; top: 48px;
    width: 1080px; height: 700px;
    display: flex;
    box-shadow: 0 6px 24px rgba(0,0,0,.15);
  }
  .panel { position: relative; width: 360px; height: 700px; background: var(--paper); overflow: hidden; }
  .panel + .panel { border-left: 1px solid #e2e2e2; }

  /* Bio panel */
  .bio { padding: 36px 36px 0; text-align: center; }
  .quote { font-family: "Montserrat", sans-serif; font-style: italic; font-size: 12px; line-height: 1.45; color: var(--ink); }
  .quote-author { margin-top: 4px; font-family: "Montserrat", sans-serif; font-weight: 700; font-size: 11px; color: var(--red); text-align: right; padding-right: 20px; }
  .quote-author::before { content: ""; display: inline-block; width: 70px; height: 1px; background: var(--red); vertical-align: middle; margin-right: 4px; }
  .portrait {
    width: 140px; height: 140px; border-radius: 50%;
    margin: 16px auto 20px;
    border: 5px solid var(--red);
    background: radial-gradient(circle at 50% 40%, #c9a48c, #7a5a48 60%, #9db58a);
  }
  .section-title { font-family: "Montserrat", sans-serif; font-weight: 800; font-size: 13px; color: var(--red); margin-bottom: 6px; letter-spacing: .3px; }
  .bio-text p { font-size: 10.5px; line-height: 1.5; margin-bottom: 10px; color: var(--ink); }

  /* Contact panel */
  .contact-wave { position: absolute; left: 0; top: 0; width: 360px; height: 330px; }
  .contact-body { position: absolute; top: 332px; left: 0; right: 0; text-align: center; padding: 0 30px; }
  .cta-title { font-family: "Montserrat", sans-serif; font-weight: 800; font-size: 19px; color: var(--red); }
  .cta-sub { font-size: 11px; line-height: 1.4; margin-top: 4px; color: var(--muted); }
  .mark-small { display: flex; flex-direction: column; align-items: center; margin-top: 18px; }
  .dot { width: 30px; height: 30px; border-radius: 50%; background: var(--leaf); }
  .agent-name { font-family: "Montserrat", sans-serif; font-weight: 700; font-size: 13px; margin-top: 6px; }
  .agent-role { font-family: "Montserrat", sans-serif; font-weight: 700; font-size: 11px; }
  .contact-lines { font-size: 10.5px; line-height: 1.5; margin-top: 4px; color: var(--muted); }
  .contact-lines span { color: var(--red); }
  .brokerage { display: inline-flex; align-items: center; gap: 6px; margin-top: 12px; font-family: "Montserrat", sans-serif; font-weight: 700; font-size: 12px; color: var(--red); }
  .brokerage i { width: 12px; height: 12px; background: var(--red); display: inline-block; }
  .address { font-size: 10.5px; line-height: 1.5; margin-top: 6px; color: var(--muted); }

  /* Cover panel */
  .cover { background: var(--paper-alt); }
  .cover-curve { position: absolute; left: 0; top: 0; width: 360px; height: 200px; }
  .cover-body { position: absolute; top: 170px; left: 0; right: 0; padding-left: 46px; }
  .cover-mark { display: flex; flex-direction: column; align-items: center; width: 230px; }
  .dot-large { width: 90px; height: 90px; border-radius: 50%; background: var(--leaf); }
  .cover-name { font-family: "Montserrat", sans-serif; font-weight: 700; font-size: 22px; margin-top: 10px; color: #222; }
  .headline { margin-top: 28px; font-family: "Montserrat", sans-serif; font-weight: 800; font-size: 32px; line-height: 1.05; }
  .headline .red { color: var(--red); display: block; }
  .headline .green { color: var(--green); display: block; }
  .call-bar { display: flex; margin-top: 24px; height: 54px; width: 290px; }
  .call-label { background: var(--green); color: #fff; font-family: "Montserrat", sans-serif; font-weight: 700; font-size: 11px; width: 66px; display: flex; align-items: center; justify-content: center; text-align: center; line-height: 1.2; }
  .call-info { background: var(--red); color: #fff; flex: 1; display: flex; flex-direction: column; justify-content: center; padding-left: 14px; font-size: 12px; line-height: 1.5; font-weight: 600; }
  .inside { margin-top: 30px; width: 290px; }
  .inside-title { font-family: "Montserrat", sans-serif; font-weight: 700; font-size: 11px; color: var(--green); letter-spacing: 1px; margin-bottom: 6px; }
  .inside-list { list-style: none; font-size: 11px; line-height: 1.7; color: var(--ink); }
  .inside-list li::before { content: ""; display: inline-block; width: 6px; height: 6px; background: var(--red); margin-right: 8px; vertical-align: middle; }
</style>
</head>
<body>
  <main class="brochure">
    <section class="panel bio">
      <p class="quote">"all our dreams can come true if<br>we have the courage to pursue them"</p>
      <p class="quote-author">Marion Hale</p>
      <div class="portrait" role="img" aria-label="Portrait photo of the agent"></div>
      <div class="bio-text">
        <h2 class="section-title">MISSION STATEMENT</h2>
        <p>I want to help you find the home of your dreams, whether it's your first home, something bigger, downsizing or anything in between. I want to be the one to help you with this significant moment in your life.</p>
        <h2 class="section-title">BIO</h2>
        <p>I am a mom to an amazing girl and wife to a wonderful husband. I moved here in the 1990s and love the Lower Mainland and the beauty it has to offer, having lived in many Greater Vancouver neighbourhoods.</p>
        <p>Passionate, driven, and committed to my clients, my market knowledge makes me an invaluable guide through the buying process. I go above and beyond and build relationships that last long past the sale.</p>
      </div>
    </section>

    <section class="panel contact">
      <svg class="contact-wave" viewBox="0 0 360 330">
        <defs>
          <linearGradient id="houseTone" x1="0" y1="0" x2="0" y2="1">
            <stop offset="0" stop-color="#c9d8e6"/>
            <stop offset=".45" stop-color="#5d6f86"/>
            <stop offset="1" stop-color="#4e7a3e"/>
          </linearGradient>
        </defs>
        <g role="img" aria-label="Photo of a two-storey blue house with trees">
          <path d="M0 0 H360 V150 C260 230 140 275 0 292 Z" fill="url(#houseTone)"/>
        </g>
        <path d="M0 292 C140 275 260 230 360 150 V172 C260 250 140 298 0 312 Z" fill="var(--red)"/>
        <path d="M0 322 C150 306 270 262 360 190" fill="none" stroke="var(--red)" stroke-width="2"/>
      </svg>
      <div class="contact-body">
        <h2 class="cta-title">READY TO GET STARTED?</h2>
        <p class="cta-sub">Call Or Email Me Today And Let's Discuss<br>Your Next Home Sale Or Purchase</p>
        <div class="mark-small">
          <div class="dot"></div>
          <p class="agent-name">Clara Whitfield</p>
        </div>
        <p class="agent-role">Personal Real Estate Corporation</p>
        <p class="contact-lines">Give me a call at <span>604-555-0143</span><br>Email me at <span>clara@teamhollowbrook.ca</span></p>
        <p class="brokerage"><i></i>Harbor Crest Realty</p>
        <p class="address">210 - 4471 Maple Crescent,<br>Port Coquitlam, BC V3C 1A1</p>
      </div>
    </section>

    <section class="panel cover">
      <svg class="cover-curve" viewBox="0 0 360 200">
        <g role="img" aria-label="Continuation of the house photo">
          <path d="M0 0 H70 C50 60 25 120 0 150 Z" fill="#8aa2b8"/>
        </g>
        <path d="M0 150 C25 120 50 60 70 0 H92 C70 75 40 140 0 172 Z" fill="var(--red)"/>
      </svg>
      <div class="cover-body">
        <div class="cover-mark">
          <div class="dot-large"></div>
          <p class="cover-name">Clara Whitfield</p>
        </div>
        <h1 class="headline"><span class="red">WHERE'S YOUR</span><span class="green">NEXT HOME?</span></h1>
        <div class="call-bar">
          <div class="call-label">CALL<br>OR TEXT</div>
          <div class="call-info"><span>778 555 0192</span><span>www.teamhollowbrook.ca</span></div>
        </div>
        <div class="inside">
          <p class="inside-title">INSIDE</p>
          <ul class="inside-list">
            <li>Mission Statement</li>
            <li>Bio</li>
            <li>Why Use a Buyer's Agent</li>
            <li>Choosing the Right Realtor</li>
          </ul>
        </div>
      </div>
    </section>
  </main>
</body>
</html>
```